Brennock transport business cards

Front of card, Looking for my logo on one side of the card

Back of card,
Brennock Transport Maintenance
Onsite Cars, Trucks & trailer maintenance and repairs
Gary Brennock
0452918406
Brennocktm@vexmail.test

```html
<!DOCTYPE html>
<html lang="en">
<head>
<meta charset="utf-8">
<title>Brennock Transport Business Cards</title>
<link rel="stylesheet" href="https://fonts.googleapis.com/css2?family=Montserrat:wght@600;700;800&display=swap">
<style>
  :root {
    --backdrop: #c9c9c9;
    --charcoal: #262626;
    --charcoal-deep: #1b1b1b;
    --blue: #1466d1;
    --blue-deep: #0b3f8a;
    --blue-dark: #08224a;
    --silver: #d9dde2;
    --white: #ffffff;
  }
  * { box-sizing: border-box; margin: 0; padding: 0; }
  html, body {
    width: 1200px; height: 788px; overflow: hidden;
    background: var(--backdrop);
    font-family: "Montserrat", Arial, sans-serif;
  }
  .canvas {
    width: 1200px; height: 788px;
    display: flex; align-items: center; justify-content: center; gap: 48px;
  }
  .card {
    position: relative;
    width: 540px; height: 310px;
    border-radius: 22px;
    overflow: hidden;
    background: var(--charcoal);
    box-shadow: 0 14px 30px rgba(0,0,0,0.28);
  }

  /* Back card: contact details */
  .back .info-band {
    position: absolute; left: 0; right: 0; top: 128px; bottom: 0;
    background: linear-gradient(160deg, var(--blue) 0%, var(--blue-deep) 60%, var(--blue-dark) 100%);
    border-top: 6px solid var(--charcoal);
    box-shadow: 0 -4px 0 var(--blue);
  }
  .back .company-block {
    position: absolute; left: 40px; top: 26px;
    color: var(--white);
  }
  .back .company-name {
    font-weight: 800; font-size: 22px; letter-spacing: 0.5px;
  }
  .back .services {
    margin-top: 6px; font-weight: 700; font-size: 17px; line-height: 1.25;
  }
  .back .contact {
    position: absolute; right: 40px; top: 168px;
    color: var(--white);
  }
  .back .person-name {
    font-weight: 800; font-size: 30px; letter-spacing: 1px; text-transform: uppercase;
  }
  .back .contact-line {
    display: flex; align-items: center; gap: 8px;
    margin-top: 8px; font-weight: 700; font-size: 18px; letter-spacing: 0.5px;
  }
  .back .contact-line svg { width: 16px; height: 16px; flex: none; }

  /* Front card: brand side */
  .front {
    background: radial-gradient(ellipse at 40% 40%, #2c3340 0%, var(--charcoal) 55%, var(--charcoal-deep) 100%);
  }
  .front .brand {
    position: absolute; left: 0; right: 0; top: 100px;
    display: flex; align-items: center; justify-content: center; gap: 16px;
  }
  .front .brand-mark {
    width: 22px; height: 22px; background: var(--blue);
  }
  .front .brand-name {
    color: var(--white); font-weight: 800; font-size: 52px; letter-spacing: 2px; text-transform: uppercase;
  }
  .front .base-band {
    position: absolute; left: 0; right: 0; bottom: 0; height: 46px;
    background: linear-gradient(180deg, var(--blue) 0%, var(--blue-deep) 100%);
    border-top: 4px solid var(--silver);
  }
</style>
</head>
<body>
<main class="canvas">
  <section class="card back" aria-label="Card back with contact details">
    <div class="company-block">
      <p class="company-name">Brennock Transport Maintenance</p>
      <p class="services">Onsite Cars, Trucks &amp; trailer<br>maintenance and repairs</p>
    </div>
    <div class="info-band"></div>
    <div class="contact">
      <p class="person-name">Gary Brennock</p>
      <p class="contact-line">
        <svg viewBox="0 0 24 24" aria-hidden="true"><path fill="#fff" d="M6.6 10.8a15 15 0 0 0 6.6 6.6l2.2-2.2a1 1 0 0 1 1-.25 11.4 11.4 0 0 0 3.6.57 1 1 0 0 1 1 1V20a1 1 0 0 1-1 1A17 17 0 0 1 3 4a1 1 0 0 1 1-1h3.5a1 1 0 0 1 1 1c0 1.25.2 2.45.57 3.6a1 1 0 0 1-.25 1z"/></svg>
        0452918406
      </p>
      <p class="contact-line">
        <svg viewBox="0 0 24 24" aria-hidden="true"><rect x="2" y="5" width="20" height="14" rx="2" fill="#fff"/><path d="M3 6l9 7 9-7" fill="none" stroke="#1466d1" stroke-width="2"/></svg>
        Brennocktm@vexmail.test
      </p>
    </div>
  </section>

  <section class="card front" aria-label="Card front with brand name">
    <div class="brand">
      <span class="brand-mark" aria-hidden="true"></span>
      <span class="brand-name">Brennock</span>
    </div>
    <div class="base-band"></div>
  </section>
</main>
</body>
</html>
```